Request for Business Card Design

Hi. My name is Marlena, I am looking for a new business card design for my company, Quorvane Sensing Systems, LLC. I really like the design you did for Tessaly Harvest and was hoping you could do something similar using our full logo and our mark. I am also open to any raised texture design using our mark. I have attached our full logo, which would need to be somewhere on the card, as well as the mark in both outline and full form, as well as our brand colors / guide. The card does not have to be white, as long as our logo and mark appear. I actually like darker colored business cards more, but am open to all options. If you are interested in working with me, please let me know. We would also take the business card design into letterhead design if you can do that.

```html
<!DOCTYPE html>
<html lang="en">
<head>
<meta charset="utf-8">
<title>Quorvane Sensing Systems – Business Card</title>
<link href="https://fonts.googleapis.com/css2?family=Barlow:wght@400;500;600;700&display=swap" rel="stylesheet">
<style>
  :root {
    --backdrop: #3a3a3c;
    --card: #1f2022;
    --ink-light: #f2f2f2;
    --ink-muted: #c9c9cb;
    --brand-blue: #1b9cc8;
    --gloss-hi: #8a8a8c;
    --gloss-lo: #2a2b2d;
  }
  * { box-sizing: border-box; margin: 0; padding: 0; }
  html, body { width: 800px; height: 1200px; overflow: hidden; }
  body {
    background: var(--backdrop);
    font-family: "Barlow", Arial, sans-serif;
    color: var(--ink-light);
    position: relative;
  }
  .card {
    position: absolute;
    left: 80px;
    width: 640px;
    height: 366px;
    background: var(--card);
    overflow: hidden;
    box-shadow: 0 10px 30px rgba(0,0,0,0.45);
  }
  .card--front { top: 150px; }
  .card--back { top: 684px; }

  /* Front */
  .front-brand {
    position: absolute;
    left: 56px;
    top: 150px;
    display: flex;
    align-items: center;
    gap: 14px;
  }
  .brand-dot {
    width: 30px; height: 30px;
    border-radius: 50%;
    background: var(--ink-light);
  }
  .brand-name {
    font-weight: 600;
    font-size: 30px;
    letter-spacing: 3px;
    line-height: 1;
    text-transform: uppercase;
  }
  .brand-tag {
    font-weight: 600;
    font-size: 9.5px;
    letter-spacing: 1px;
    text-transform: uppercase;
    margin-top: 4px;
  }
  .front-decoration {
    position: absolute;
    right: -70px;
    top: 40px;
    width: 380px;
    height: 380px;
  }

  /* Back */
  .holder {
    position: absolute;
    left: 44px;
    top: 66px;
  }
  .holder-name {
    color: var(--brand-blue);
    font-weight: 700;
    font-size: 27px;
    letter-spacing: 1px;
    text-transform: uppercase;
    line-height: 1.05;
  }
  .holder-role {
    font-weight: 700;
    font-size: 15px;
    letter-spacing: 1.5px;
    text-transform: uppercase;
    margin-top: 4px;
  }
  .holder-rule {
    width: 52px;
    height: 3px;
    background: var(--brand-blue);
    margin: 16px 0 14px;
  }
  .contact-list { list-style: none; font-size: 17px; line-height: 1.35; }
  .contact-label { color: var(--brand-blue); display: inline-block; width: 20px; }
  .back-brand {
    position: absolute;
    right: 44px;
    top: 70px;
    display: flex;
    align-items: center;
    gap: 14px;
  }
  .back-brand .brand-dot { background: var(--brand-blue); width: 40px; height: 40px; }
  .back-brand .brand-name { font-size: 32px; }
  .address {
    position: absolute;
    right: 44px;
    bottom: 40px;
    text-align: right;
    font-size: 19px;
    line-height: 1.3;
  }
  .address-web { color: var(--brand-blue); font-weight: 500; }
</style>
</head>
<body>

<section class="card card--front">
  <div class="front-brand">
    <span class="brand-dot"></span>
    <div>
      <div class="brand-name">Quorvane</div>
      <div class="brand-tag">Sensing Systems</div>
    </div>
  </div>
  <svg class="front-decoration" viewBox="0 0 380 380" aria-hidden="true">
    <defs>
      <linearGradient id="gloss" x1="0" y1="0" x2="1" y2="1">
        <stop offset="0" stop-color="var(--gloss-hi)"/>
        <stop offset="0.55" stop-color="#4a4a4c"/>
        <stop offset="1" stop-color="var(--gloss-lo)"/>
      </linearGradient>
    </defs>
    <circle cx="190" cy="190" r="180" fill="url(#gloss)"/>
  </svg>
</section>

<section class="card card--back">
  <div class="holder">
    <div class="holder-name">Elias Vorhagen</div>
    <div class="holder-role">Managing Director</div>
    <div class="holder-rule"></div>
    <ul class="contact-list">
      <li><span class="contact-label">P</span>555 214 36 70</li>
      <li><span class="contact-label">M</span>888 407 19 62</li>
      <li><span class="contact-label">E</span>e.vorhagen@quorvane.com</li>
    </ul>
  </div>
  <div class="back-brand">
    <span class="brand-dot"></span>
    <div>
      <div class="brand-name">Quorvane</div>
      <div class="brand-tag">Sensing Systems</div>
    </div>
  </div>
  <address class="address" style="font-style:normal">
    <div>48 Harlow Lane</div>
    <div>Brookfield, New York 12408</div>
    <div class="address-web">www.quorvane.com</div>
  </address>
</section>

</body>
</html>
```